Design a Website Mockup for a film & video production company

Who we are...
Quarrystone Pictures is a growing video production company that has been running for almost 8 years. We are well established but looking to update our online presence to match our new logo and branding. Quarrystone Pictures specializes in high definition commercial, corporate, music video, real estate and broadcast work. We also do editing and motion graphics work and have an ever expanding 3D portfolio.

What we need...
We need a new web site design (for web and mobile devices) that reflects the quality of our work but also the fun and creative attitude of our people. We can provide branding colours and logo as well as sample video content and team photos for the website.

The design and interface should be:
Innovative
Clean
Contemporary
Sleek
Fun
Easy to use and navigate
Flexible to add to
Work within a HTML 5 design implementation
And appears bespoke or custom.

We will need multiple pages as part of the final design. Our current website can be used as an indication of the number of pages and Type of content we need but we want to the pages to stand out as we do not like the layout at all currently.

Our current website is

Much of the design must centre around video content. Our videos typically have two sizes that we use on the website. 640x360 and 1280x720

We are open to any design ideas and want you to be creative in what you do. We like websites that have large photo or visual backgrounds or a strong production feel and polished finish however the right design will be fun and professional and say a lot about what we do and the quality of work we produce through the look rather than just the text content. The website should be designed in a way that allows for people to get information quickly and then get more information if they require.

We are happy to provide more information, feedback and branding elements to anyone that wants to email us.

Please find attached to this contest our logo as an EPS and our credits so you get an idea of the look we are going for. You can use screenshots from the video as placeholders on the website.

Please email:
Info@quarrystonepictures.example

```html
<!DOCTYPE html>
<html lang="en">
<head>
<meta charset="utf-8">
<title>Quarrystone Pictures — About Us</title>
<link href="https://fonts.googleapis.com/css2?family=PT+Sans:wght@400;700&display=swap" rel="stylesheet">
<style>
  :root {
    --sidebar-bg: #151515;
    --sidebar-line: #1d1d1d;
    --brand-red: #b0232a;
    --nav-text: #8d8d8d;
    --nav-active: #ffffff;
    --panel-bg: #ffffff;
    --title-text: #333333;
    --body-text: #555555;
    --rule: #d9d9d9;
    --photo-light: #ecebe8;
    --photo-mid: #d5d4d0;
    --photo-dark: #b9b8b4;
  }
  * { margin: 0; padding: 0; box-sizing: border-box; }
  html, body { width: 1200px; height: 493px; overflow: hidden; }
  body { font-family: "PT Sans", Arial, sans-serif; background: var(--photo-light); position: relative; }

  .hero-photo {
    position: absolute; left: 720px; top: 0; width: 480px; height: 493px;
    background: radial-gradient(ellipse at 70% 55%, var(--photo-light) 0%, var(--photo-mid) 60%, var(--photo-dark) 100%);
  }

  .sidebar {
    position: absolute; left: 0; top: 0; width: 201px; height: 493px;
    background: repeating-linear-gradient(0deg, var(--sidebar-bg) 0 2px, var(--sidebar-line) 2px 3px);
  }
  .sidebar-edge { position: absolute; left: 201px; top: 0; width: 10px; height: 493px; background: var(--brand-red); }

  .brand {
    position: absolute; left: 14px; top: 44px; width: 180px;
    color: #ffffff; font-weight: 700; font-size: 19px; line-height: 21px;
    display: flex; align-items: center; gap: 8px;
  }
  .brand-mark { width: 12px; height: 12px; background: var(--brand-red); flex: none; }

  .main-nav { position: absolute; left: 17px; top: 122px; width: 185px; list-style: none; }
  .main-nav li {
    height: 29px; line-height: 29px; padding: 0 14px 0 13px;
    font-size: 11px; text-transform: uppercase; color: var(--nav-text);
    display: flex; justify-content: space-between;
  }
  .main-nav li.is-active { background: var(--brand-red); color: var(--nav-active); }
  .main-nav .plus { font-size: 11px; }
  .buy-link {
    position: absolute; left: 30px; top: 395px;
    color: var(--nav-text); font-weight: 700; font-size: 12px; text-transform: uppercase;
  }

  .player { position: absolute; left: 17px; top: 451px; width: 184px; height: 28px; display: flex; align-items: center; }
  .player-note { width: 27px; height: 28px; background: var(--brand-red); display: flex; align-items: center; justify-content: center; }
  .player-controls { display: flex; align-items: center; gap: 12px; margin-left: 10px; }
  .player-track { width: 52px; height: 2px; background: #3a3a3a; margin-left: 14px; position: relative; }
  .player-track::after { content: ""; position: absolute; right: 0; top: 0; width: 20px; height: 2px; background: #777; }

  .panel-toggle {
    position: absolute; left: 211px; top: 51px; width: 11px; height: 26px;
    background: var(--brand-red); display: flex; align-items: center; justify-content: center;
  }

  .content { position: absolute; left: 211px; top: 0; width: 509px; height: 493px; background: var(--panel-bg); overflow: hidden; }
  .page-title {
    position: absolute; left: 39px; top: 36px;
    font-weight: 400; font-size: 21px; letter-spacing: 0.5px; color: var(--title-text);
  }
  .rule { position: absolute; left: 39px; width: 431px; height: 1px; background: var(--rule); }
  .rule.top { top: 78px; }
  .rule.bottom { top: 277px; }
  .feature-band {
    position: absolute; left: 37px; top: 97px; width: 435px; height: 160px;
    background: var(--brand-red); display: flex; align-items: center; justify-content: center;
  }
  .copy { position: absolute; left: 39px; top: 296px; width: 431px; }
  .copy p { font-size: 10.6px; line-height: 19.3px; color: var(--body-text); text-align: justify; margin-bottom: 12px; }
</style>
</head>
<body>
  <div class="hero-photo" role="img" aria-label="Photograph of a white electrical plug held by a robotic arm reaching toward a wall socket"></div>

  <aside class="sidebar">
    <div class="brand"><span class="brand-mark"></span><span>Quarrystone Pictures</span></div>
    <ul class="main-nav">
      <li>Home<span class="plus">+</span></li>
      <li class="is-active">About Us<span class="plus">+</span></li>
      <li>News</li>
      <li>Portfolio</li>
      <li>Our Projects<span class="plus">+</span></li>
      <li>Showreel</li>
      <li>Galleries<span class="plus">+</span></li>
      <li>Features<span class="plus">+</span></li>
      <li>Contact Us</li>
    </ul>
    <div class="buy-link">Buy this theme!</div>
    <div class="player">
      <div class="player-note">
        <svg width="12" height="12" viewBox="0 0 12 12"><path d="M4 1 L11 0 V8.5 A1.8 1.8 0 1 1 9.6 6.8 V2.4 L5.4 3 V10 A1.8 1.8 0 1 1 4 8.3 Z" fill="#fff"/></svg>
      </div>
      <div class="player-controls">
        <svg width="10" height="7" viewBox="0 0 10 7"><path d="M5 0 L0 3.5 L5 7Z M10 0 L5 3.5 L10 7Z" fill="#ddd"/></svg>
        <svg width="8" height="9" viewBox="0 0 8 9"><path d="M0 0 L8 4.5 L0 9Z" fill="#ddd"/></svg>
        <svg width="10" height="7" viewBox="0 0 10 7"><path d="M0 0 L5 3.5 L0 7Z M5 0 L10 3.5 L5 7Z" fill="#ddd"/></svg>
        <svg width="7" height="7" viewBox="0 0 7 7"><path d="M0 2 H2 L4.5 0 V7 L2 5 H0Z" fill="#ddd"/></svg>
      </div>
      <div class="player-track"></div>
    </div>
  </aside>
  <div class="sidebar-edge"></div>

  <main class="content">
    <h1 class="page-title">ABOUT US</h1>
    <div class="rule top"></div>
    <div class="feature-band">
      <svg width="112" height="82" viewBox="0 0 112 82">
        <circle cx="33" cy="16" r="16" fill="#fff"/>
        <circle cx="67" cy="16" r="16" fill="#fff"/>
        <rect x="12" y="34" width="74" height="48" rx="5" fill="#fff"/>
        <rect x="0" y="46" width="8" height="22" rx="3" fill="#fff"/>
        <path d="M86 52 L112 34 V82 L86 66Z" fill="#fff"/>
      </svg>
    </div>
    <div class="rule bottom"></div>
    <div class="copy">
      <p>Pellentesque diam lectus, dapibus non lacinia in, vulputate sit amet dolor. Vivamus sollicitudin nunc sed augue lobortis at elementum nulla tristique. Sed elit elit, adipiscing eget molestie vulputate, euismod vitae mi. Proin posuere volutpat congue. Proin posuere volutpat congue.</p>
      <p>Phasellus rhoncus, nunc vel lobortis faucibus, arcu elit rutrum metus, ut molestie nisi nisl ac ligula. Etiam eget nibh non tellus commodo adipiscing. Quisque pharetra lorem nec massa ornare rhoncus. Vivamus auctor aliquet lacus, adipiscing dignissim lectus volutpat sed. Maecenas viverra sapien et mi venenatis dignissim egestas justo posuere. Morbi hendrerit aliquam diam a rhoncus. Vivamus luctus aliquam orci vitae semper. Ut euismod dolor in lectus pulvinar, non ultrices nulla consequat integer.</p>
    </div>
  </main>
  <div class="panel-toggle">
    <svg width="6" height="10" viewBox="0 0 6 10"><path d="M1 1 L5 5 L1 9" stroke="#fff" stroke-width="1.5" fill="none"/></svg>
  </div>
</body>
</html>
```